Brightvale Assist Public Benefit Corporation - Initial Website

We need to develop an initial website for Brightvale Assist PBC. We are a startup managed business services provider focused on small business owners, entrepreneurs and their employees. We are a public benefit corporation and our public mission is to help business owners, entrepreneurs and their employees overcome the challenges that hold them back from reaching personal and professional success.
Our primary service offerings are managed business services that allow us to support the day-to-day operations of the businesses we support. This ongoing support provides the necessary pre-requisite relationship so we can provide effective and timely support when their organizations are experiencing challenges and moments of crisis. In those moments, it is our opportunity to help them overcome those challenges and stay on track for business utopia.
Our services are provided on a contract basis for a fixed monthly fee. We want to build strong relationships that help our clients grow their businesses while taking away the stresses associated with the backend of the business operations.
Finally, our public benefit is that we provide crisis invention, critical incident support, and mental health services to business owners and their employees during challenging times in an effort to improve their overall quality of life.

Coding

Coded - Design and coding required

```html
<!DOCTYPE html>
<html lang="en">
<head>
<meta charset="utf-8">
<title>Brightvale Assist PBC</title>
<link href="https://fonts.googleapis.com/css2?family=Montserrat:wght@500;600;700&family=Poppins:wght@400;500;600&display=swap" rel="stylesheet">
<style>
:root{
  --orange:#fa7000;
  --navy:#0b1a4f;
  --ink:#111827;
  --muted:#4b5563;
  --line:#e5e7eb;
  --soft:#f7f7f7;
  --white:#ffffff;
}
*{box-sizing:border-box;margin:0;padding:0}
html,body{width:1200px;height:4743px;overflow:hidden}
body{position:relative;font-family:'Poppins',sans-serif;color:var(--ink);background:var(--white)}
.abs{position:absolute}
h1,h2,h3,.head{font-family:'Montserrat',sans-serif}
.label{font-size:12px;font-weight:500;color:var(--orange);text-transform:uppercase;display:flex;align-items:center;gap:8px}
.label::before{content:"";width:7px;height:7px;border-radius:50%;background:var(--orange)}
.btn{display:inline-flex;align-items:center;justify-content:center;border-radius:20px;font-size:13px;font-weight:500}
.btn-orange{background:var(--orange);color:#fff}

/* header */
.site-header{top:0;left:0;width:1200px;height:80px;background:#fff;box-shadow:0 2px 8px rgba(0,0,0,.06);z-index:3}
.brand{font-family:'Poppins',sans-serif;font-weight:600;color:var(--orange);display:flex;align-items:center;gap:8px}
.brand .dot{width:12px;height:12px;border-radius:50%;background:var(--orange)}
.brand .name{font-size:24px;line-height:1}
.brand .sub{font-size:10px;letter-spacing:.3px;line-height:1.2;text-transform:uppercase}
.site-nav{left:452px;top:32px;display:flex;gap:0;font-size:12px;font-weight:500}
.site-nav span{position:absolute;white-space:nowrap}
.caret{display:inline-block;margin-left:6px;border:4px solid transparent;border-top:5px solid var(--ink);vertical-align:-2px}
.header-cta{left:924px;top:22px;width:134px;height:36px;gap:8px}

/* hero */
.hero{top:80px;left:0;width:1200px;height:574px;background:linear-gradient(90deg,#f4f4f2 0%,#eeeeea 40%,#c9a98a 62%,#8d6b52 80%,#d9c6b0 100%)}
.hero h1{left:138px;top:140px;font-size:55px;line-height:64px;font-weight:700;color:var(--ink)}
.hero p{left:138px;top:282px;width:490px;font-size:14px;line-height:26px;color:var(--ink)}
.hero .b1{left:138px;top:360px;width:134px;height:38px}
.hero .b2{left:293px;top:360px;width:203px;height:38px;border:1.5px solid var(--navy);color:var(--navy);background:#fff}
.scroll{left:62px;top:545px;width:24px;height:160px}
.scroll .bar{position:absolute;left:8px;top:0;width:1px;height:62px;background:var(--ink)}
.scroll .arrow{position:absolute;left:5px;top:64px;border:4px solid transparent;border-top:6px solid var(--orange)}
.scroll span{position:absolute;left:-28px;top:112px;transform:rotate(90deg);font-size:8px;font-weight:600;white-space:nowrap}

.goal{top:740px;left:0;width:1200px;text-align:center;font-size:15px;color:var(--muted);text-transform:uppercase}
.goal em{font-style:normal;color:var(--orange)}
.rule{top:804px;left:0;width:1200px;height:1px;background:var(--line)}

/* services */
.svc-label{left:141px;top:858px}
.svc-title{left:138px;top:882px;font-size:36px;line-height:48px;font-weight:600;width:420px}
.stat{width:202px}
.stat .num{font-family:'Montserrat',sans-serif;font-size:50px;font-weight:500;color:var(--orange);display:flex;align-items:flex-start;gap:12px;line-height:1}
.stat .num small{font-size:12px;color:var(--ink);margin-top:6px}
.stat .bar{height:1px;background:var(--line);margin:22px 0 16px}
.stat p{font-size:12px;line-height:20px;color:#333}
.svc-card{top:1065px;width:288px;text-align:center}
.svc-card .photo{height:148px;box-shadow:0 4px 10px rgba(0,0,0,.12)}
.svc-card h3{font-family:'Poppins',sans-serif;font-size:16px;font-weight:500;margin-top:26px}
.svc-card p{font-size:12px;line-height:19px;color:var(--muted);margin:12px auto 0;width:240px}
.view-all{left:511px;top:1350px;display:flex;align-items:center;gap:16px;font-size:14px;font-weight:600}
.view-all .circ{width:38px;height:38px;border-radius:50%;background:var(--orange);display:flex;align-items:center;justify-content:center}
.tower{left:937px;top:1290px;width:263px;height:189px;background:linear-gradient(135deg,transparent 30%,#cfcfcf 31%,#8a8a8a 70%,#5f5f5f 100%)}

/* about */
.about{top:1479px;left:0;width:1200px;height:560px;background:var(--soft)}
.about-photo{left:141px;top:1552px;width:444px;height:388px;background:linear-gradient(135deg,#e9e5df 0%,#d6cfc6 45%,#f38a2c 46%,#fa7000 70%,#cfc8bf 71%,#b9b3ab 100%)}
.about-label{left:625px;top:1574px}
.about h2{position:absolute;left:625px;top:122px;font-size:38px;font-weight:600}
.about p{position:absolute;left:625px;width:440px;font-size:13px;line-height:22.5px;color:#333}
.about .btn{position:absolute;left:625px;top:426px;width:134px;height:36px}

/* testimonials */
.testi{top:2039px;left:0;width:1200px;height:576px;background:var(--navy);overflow:hidden}
.testi .label{position:absolute;left:0;width:1200px;top:88px;justify-content:center;color:#fff}
.testi .label::before{background:#fff}
.testi h2{position:absolute;top:112px;width:1200px;text-align:center;color:#fff;font-size:36px;font-weight:600}
.t-card{top:197px;height:224px;background:#fff;padding:30px 34px}
.t-card h3{font-size:17px;font-weight:600}
.t-card .role{font-size:11px;color:var(--muted);margin-top:4px}
.t-card .stars{position:absolute;top:34px;right:38px;color:var(--orange);font-size:14px;letter-spacing:1px}
.t-card p{font-size:11.5px;line-height:19px;color:#333;margin-top:22px}
.avatar{width:75px;height:75px;border-radius:50%;background:linear-gradient(135deg,#e7e2dc,#b9ab9b);border:3px solid #fff}
.dots{top:470px;left:567px;display:flex;gap:8px}
.dots i{width:9px;height:9px;border-radius:50%;background:#8b93b0}
.dots i:first-child{background:#fff}

/* why */
.why{top:2615px;left:0;width:1200px;height:633px;background:var(--soft)}
.why .label{position:absolute;top:98px;width:1200px;justify-content:center}
.why h2{position:absolute;top:122px;width:1200px;text-align:center;font-size:37px;line-height:49px;font-weight:600}
.why .lead{position:absolute;top:235px;left:150px;width:900px;text-align:center;font-size:12.5px;line-height:22px;color:#333}
.feat{width:276px;height:78px;background:#fff;border:1px solid var(--line);display:flex;align-items:center;gap:22px;padding-left:24px;font-size:14px;font-weight:500}
.feat .ic{width:46px;height:46px;border-radius:50%;display:flex;align-items:center;justify-content:center;flex:none}
.ic.o{background:var(--orange)} .ic.n{background:var(--navy)}

/* cta */
.cta{top:3248px;left:0;width:1200px;height:622px;background:var(--orange)}
.cta h2{position:absolute;left:138px;top:116px;font-size:37px;line-height:49px;color:#fff;font-weight:600;width:560px}
.worldmap{left:717px;top:3355px;width:368px;height:150px;background:radial-gradient(ellipse at 30% 50%,rgba(255,255,255,.9) 0,rgba(255,255,255,.55) 45%,transparent 70%),radial-gradient(ellipse at 75% 45%,rgba(255,255,255,.9) 0,rgba(255,255,255,.5) 45%,transparent 70%)}
.lower{top:3870px;left:0;width:1200px;height:370px;background:var(--soft)}
.quote{top:3583px;left:141px;width:917px;height:561px;background:#fff;border-radius:10px;box-shadow:0 6px 24px rgba(0,0,0,.08);overflow:hidden}
.quote-photo{position:absolute;left:0;top:0;width:353px;height:561px;background:linear-gradient(160deg,#e9e4dc 0%,#cfc7bb 40%,#3a4ea8 70%,#1f2f7a 100%)}
.quote h2{position:absolute;left:404px;top:34px;font-size:29px;font-weight:600}
.field{position:absolute;left:404px;width:466px}
.field label{display:block;font-size:13px;margin-left:6px}
.field label b{color:var(--orange);font-weight:400}
.field .input{margin-top:10px;height:40px;border:1px solid var(--line);border-radius:4px;background:#fafafa;font-size:11px;color:#9ca3af;padding:13px 20px}
.field .input.filled{color:var(--ink)}
.quote .submit{position:absolute;left:404px;top:475px;width:466px;height:48px;border-radius:6px;background:var(--orange);color:#fff;font-size:11px;font-weight:600;display:flex;align-items:center;justify-content:center}

/* footer */
.site-footer{top:4240px;left:0;width:1200px;height:503px;background:var(--navy);color:#fff}
.site-footer .brand{position:absolute;left:138px;top:88px}
.f-about{position:absolute;left:400px;top:100px;width:480px;font-size:12.5px;line-height:22px}
.socials{position:absolute;left:927px;top:95px;display:flex;gap:14px}
.socials i{width:34px;height:34px;border-radius:50%;background:#2a3870}
.socials i.on{background:var(--orange)}
.f-rule{position:absolute;left:138px;width:920px;height:1px;background:#3b4676}
.f-head{position:absolute;top:212px;width:1200px;text-align:center;font-size:13px;font-weight:500}
.f-col{position:absolute;top:268px;width:277px;text-align:center}
.f-col h4{font-size:12.5px;font-weight:500;margin-top:10px}
.f-col p{font-size:12.5px;line-height:20px;color:#c8cde0;margin-top:14px}
.f-div{position:absolute;top:260px;width:1px;height:118px;background:#3b4676}
.copy{position:absolute;left:138px;top:458px;font-size:12px}
.f-nav{position:absolute;top:458px;left:642px;font-size:12px;display:flex;gap:32px;color:#c8cde0}
.f-nav span:first-child{color:#fff}
</style>
</head>
<body>

<header class="site-header abs">
  <div class="brand abs" style="left:138px;top:22px">
    <span class="dot"></span>
    <div><div class="name">Brightvale Assist</div><div class="sub">Public Benefit Corporation</div></div>
  </div>
  <nav class="site-nav abs">
    <span style="left:0">Home<i class="caret"></i></span>
    <span style="left:96px">About Us<i class="caret"></i></span>
    <span style="left:210px">Our Services<i class="caret"></i></span>
    <span style="left:346px">Testimonials<i class="caret"></i></span>
  </nav>
  <a class="btn btn-orange header-cta abs">
    <svg width="13" height="13" viewBox="0 0 24 24" fill="#fff"><path d="M6.6 10.8a15.1 15.1 0 0 0 6.6 6.6l2.2-2.2c.3-.3.7-.4 1-.2 1.1.4 2.3.6 3.6.6.6 0 1 .4 1 1V20c0 .6-.4 1-1 1A17 17 0 0 1 3 4c0-.6.4-1 1-1h3.5c.6 0 1 .4 1 1 0 1.3.2 2.5.6 3.6.1.3 0 .7-.2 1z"/></svg>
    Contact Us
  </a>
</header>

<section class="hero abs" role="img" aria-label="Photo of three colleagues reviewing documents together at an office desk">
  <h1 class="abs">Empowering Your<br>Business Journey</h1>
  <p class="abs">Providing managed business services and critical support to help you navigate challenges, crises, and moments of growth</p>
  <a class="btn btn-orange b1 abs">Contact Us</a>
  <a class="btn b2 abs">Learn How We Can Help</a>
</section>
<div class="scroll abs"><div class="bar"></div><div class="arrow"></div><span>SCROLL DOWN</span></div>

<p class="goal abs">Our goal is to empower small businesses with services and <em>support for success.</em></p>
<div class="rule abs"></div>

<div class="label svc-label abs">Services We Provide</div>
<h2 class="svc-title abs">Focused Solutions for Your Business Success.</h2>
<div class="stat abs" style="left:607px;top:884px">
  <div class="num">435<small>Million</small></div><div class="bar"></div>
  <p>Information on 400+ million companies worldwide.</p>
</div>
<div class="stat abs" style="left:856px;top:884px">
  <div class="num">100<small>Percent</small></div><div class="bar"></div>
  <p>Overall client satisfaction survey</p>
</div>
<div class="svc-card abs" style="left:141px">
  <div class="photo" role="img" aria-label="Photo of two businessmen talking in an office" style="background:linear-gradient(135deg,#cfd6dc,#5c6670)"></div>
  <h3>Operations Management</h3><p>Streamlining backend operations for smooth daily functioning</p>
</div>
<div class="svc-card abs" style="left:456px">
  <div class="photo" role="img" aria-label="Photo of hands over a paper reading crisis" style="background:linear-gradient(135deg,#e8d9cc,#b5523f)"></div>
  <h3>Crisis Intervention</h3><p>Immediate assistance during critical incidents to keep your business on track.</p>
</div>
<div class="svc-card abs" style="left:771px">
  <div class="photo" role="img" aria-label="Photo of one person comforting another by holding hands" style="background:linear-gradient(135deg,#e4ddd5,#b49a84)"></div>
  <h3>Mental Health Support</h3><p>Caring for business owners and employees during stressful periods</p>
</div>
<div class="view-all abs">
  <span class="circ"><svg width="16" height="16" viewBox="0 0 24 24" fill="none" stroke="#fff" stroke-width="2.5"><path d="M4 12h15M13 6l6 6-6 6"/></svg></span>View All Services
</div>
<div class="tower abs" role="img" aria-label="Photo of a tall office building seen from below"></div>

<section class="about abs">
  <h2>Brightvale Assist PBC</h2>
  <p style="top:182px">At Brightvale Assist PBC, we are committed to helping small business owners and entrepreneurs thrive by offering tailored business management services and critical crisis support. As a Public Benefit Corporation, we go beyond typical business solutions—our focus is on building long-term relationships that support both the professional growth and personal well-being of our clients.</p>
  <p style="top:332px">Through our fixed monthly fee model, we provide ongoing operational support, strategic guidance, and intervention during challenging times.</p>
  <a class="btn btn-orange">Learn More</a>
</section>
<div class="about-photo abs" role="img" aria-label="Photo of a smiling woman with glasses using a laptop, with orange accent blocks"></div>
<div class="label about-label abs">About Us</div>

<section class="testi abs">
  <div class="label">Client Testimonials</div>
  <h2>What Clients Say</h2>
  <div class="t-card abs" style="left:0;width:340px;padding-left:18px">
    <h3>Nadia Corwell</h3><div class="role">Manager</div><div class="stars">★★★★☆</div>
    <p>Lorem Ipsum is simply dummy text of the printing and typesetting industry. Lorem Ipsum has been the industry's standard dummy text ever since the 1500s, when an unknown printer took</p>
  </div>
  <div class="avatar abs" role="img" aria-label="Portrait photo of the client" style="left:362px;top:217px"></div>
  <div class="t-card abs" style="left:414px;width:382px">
    <h3>Helena Vasquez</h3><div class="role">Designer</div><div class="stars">★★★★☆</div>
    <p>Lorem Ipsum is simply dummy text of the printing and typesetting industry. Lorem Ipsum has been the industry's standard dummy text ever since the 1500s, when an unknown printer took</p>
  </div>
  <div class="avatar abs" role="img" aria-label="Portrait photo of the client" style="left:816px;top:217px"></div>
  <div class="t-card abs" style="left:869px;width:382px">
    <h3>Tobias Rennick</h3><div class="role">CEO at Corvane Labs</div><div class="stars" style="right:70px">★★★★★</div>
    <p>Lorem Ipsum is simply dummy text of the printing and typesetting industry. Lorem Ipsum has been the industry's standard dummy text ever since the 1500s, when an unknown printer took</p>
  </div>
  <div class="dots abs"><i></i><i></i><i></i><i></i></div>
</section>

<section class="why abs">
  <div class="label">Why Choose Us</div>
  <h2>Transforming Challenges into<br>Opportunities Together</h2>
  <p class="lead">Brightvale Assist PBC stands apart by offering a unique fixed monthly fee model that fosters a strong, ongoing relationship with our clients. This approach allows us to provide consistent support tailored to the specific needs of small business owners and entrepreneurs, enabling them to focus on growth while we manage the complexities of their day-to-day operations.</p>
  <div class="feat abs" style="left:141px;top:341px"><span class="ic o"><svg width="20" height="20" viewBox="0 0 24 24" fill="none" stroke="#fff" stroke-width="2"><path d="M3 17h6l6-4M12 3v8M9 6h5"/></svg></span>Predictable Costs</div>
  <div class="feat abs" style="left:463px;top:341px"><span class="ic n"><svg width="20" height="20" viewBox="0 0 24 24" fill="none" stroke="#fff" stroke-width="2"><circle cx="12" cy="8" r="3"/><path d="M5 19c1-4 13-4 14 0"/></svg></span>Stress Reduction</div>
  <div class="feat abs" style="left:785px;top:341px"><span class="ic o"><svg width="20" height="20" viewBox="0 0 24 24" fill="none" stroke="#fff" stroke-width="2"><path d="M3 18h7l5-4"/><circle cx="16" cy="8" r="4"/></svg></span>Crisis Support Costs</div>
  <div class="feat abs" style="left:141px;top:453px"><span class="ic n"><svg width="20" height="20" viewBox="0 0 24 24" fill="none" stroke="#fff" stroke-width="2"><circle cx="12" cy="12" r="3"/><circle cx="12" cy="12" r="8" stroke-dasharray="4 2"/></svg></span>Personalized Solutions</div>
  <div class="feat abs" style="left:463px;top:453px"><span class="ic o"><svg width="20" height="20" viewBox="0 0 24 24" fill="#fff"><rect x="5" y="12" width="3" height="7"/><rect x="10.5" y="9" width="3" height="10"/><rect x="16" y="5" width="3" height="14"/></svg></span>Facilitation Of Growth</div>
  <div class="feat abs" style="left:785px;top:453px"><span class="ic n"><svg width="20" height="20" viewBox="0 0 24 24" fill="#fff"><rect x="4" y="8" width="16" height="11" rx="2"/><rect x="9" y="5" width="6" height="3" fill="none" stroke="#fff" stroke-width="2"/></svg></span>Enhanced Work</div>
</section>

<section class="cta abs">
  <h2>Reach Out Today and Let’s Build Your Business Success Together</h2>
</section>
<div class="worldmap abs" role="img" aria-label="White world map illustration"></div>
<div class="lower abs"></div>

<section class="quote abs">
  <div class="quote-photo" role="img" aria-label="Photo of a man and a woman working together at a laptop"></div>
  <h2>Get A Free Quote Here</h2>
  <div class="field" style="top:90px"><label>Your Name<b>*</b></label><div class="input filled">Marisol Dane |</div></div>
  <div class="field" style="top:184px"><label>Email Address<b>*</b></label><div class="input">Enter email address</div></div>
  <div class="field" style="top:278px"><label>Phone Number<b>*</b></label><div class="input">Enter your number</div></div>
  <div class="field" style="top:372px"><label>Message</label><div class="input">Enter discription</div></div>
  <div class="submit">Book Appointment</div>
</section>

<footer class="site-footer abs">
  <div class="brand">
    <span class="dot"></span>
    <div><div class="name">Brightvale Assist</div><div class="sub">Public Benefit Corporation</div></div>
  </div>
  <p class="f-about">Supporting small businesses with tailored services and crisis intervention for lasting success.</p>
  <div class="socials"><i></i><i class="on"></i><i></i></div>
  <div class="f-rule" style="top:170px"></div>
  <div class="f-head">CONTACT INFORMATION</div>
  <div class="f-col" style="left:148px">
    <svg width="18" height="18" viewBox="0 0 24 24" fill="#fa7000"><path d="M6.6 10.8a15.1 15.1 0 0 0 6.6 6.6l2.2-2.2c.3-.3.7-.4 1-.2 1.1.4 2.3.6 3.6.6.6 0 1 .4 1 1V20c0 .6-.4 1-1 1A17 17 0 0 1 3 4c0-.6.4-1 1-1h3.5c.6 0 1 .4 1 1 0 1.3.2 2.5.6 3.6.1.3 0 .7-.2 1z"/></svg>
    <h4>CALL US</h4><p>(555)-014-2368</p>
  </div>
  <div class="f-div" style="left:415px"></div>
  <div class="f-col" style="left:456px">
    <svg width="18" height="18" viewBox="0 0 24 24" fill="#fa7000"><path d="M3 11 12 3l9 8h-3v9h-4v-6h-4v6H6v-9z"/></svg>
    <h4>FIND US</h4><p>123, Lorem Ipsum is simply dummy<br>text of the printing</p>
  </div>
  <div class="f-div" style="left:782px"></div>
  <div class="f-col" style="left:772px">
    <svg width="18" height="18" viewBox="0 0 24 24" fill="#fa7000"><rect x="3" y="5" width="18" height="14" rx="1"/><path d="M3 6l9 7 9-7" fill="none" stroke="#0b1a4f" stroke-width="1.5"/></svg>
    <h4>EMAIL ADDRESS</h4><p>info@brightvaleassist.com</p>
  </div>
  <div class="f-rule" style="top:420px"></div>
  <div class="copy">Copyright © 2024 Brightvale Assist | All Right Reserved.</div>
  <nav class="f-nav"><span>Home</span><span>About us</span><span>Services</span><span>Testimonials</span><span>Contact Us</span></nav>
</footer>

</body>
</html>
```